Web Design Project

We are looking to for a redesign for www.tavelon.com. Tavelon Systems is a Managed Service Provider of IT solutions based is Calgary, Alberta, Canada. We are currently expanding into the Edmonton market and would like to lauch our new site with our expansion.
The design should be sleak in style and communicate a professional vision to our clients and prospects.

Thanks,
Derek

Target Market(s)

Small to medium size businesses looking to outsource or complement their IT solutions.

Industry/Entity Type

It Professional

```html
<!DOCTYPE html>
<html lang="en">
<head>
<meta charset="utf-8">
<title>Tavelon Systems — Managed IT Services</title>
<link href="https://fonts.googleapis.com/css2?family=Lato:wght@300;400;700&family=Orbitron:wght@500;700&display=swap" rel="stylesheet">
<style>
  :root {
    --ink: #1c1c1c;
    --text: #333333;
    --muted: #555555;
    --accent: #c0102a;
    --banner: #2f333b;
    --banner-edge: #050505;
    --rule: #dcdcdc;
    --card-border: #e2e2e2;
    --footer-bg: #f2f2f2;
    --button-bg: #ececec;
    --white: #ffffff;
  }
  * { box-sizing: border-box; margin: 0; padding: 0; }
  html, body { width: 1200px; height: 1039px; overflow: hidden; background: var(--white); }
  body { position: relative; font-family: "Lato", sans-serif; color: var(--text); }

  .top-rule { position: absolute; left: 0; top: 0; width: 1200px; height: 6px; background: var(--rule); }

  .site-header { position: absolute; left: 0; top: 6px; width: 1200px; height: 115px; }
  .brand { position: absolute; left: 78px; top: 40px; display: flex; align-items: center; gap: 14px; }
  .brand-mark { width: 40px; height: 40px; background: var(--accent); }
  .brand-name { font-family: "Lato", sans-serif; font-weight: 700; font-size: 40px; letter-spacing: 6px; color: var(--ink); line-height: 1; }

  .main-nav { position: absolute; right: 90px; top: 54px; display: flex; align-items: center; }
  .main-nav a { font-size: 15px; font-weight: 400; color: var(--muted); text-decoration: none; text-transform: uppercase; }
  .main-nav a.is-current { color: var(--ink); }
  .main-nav .sep { width: 1px; height: 20px; background: #bbb; transform: rotate(22deg); margin: 0 19px; }

  .hero { position: absolute; left: 0; top: 121px; width: 1200px; height: 420px; background: var(--banner-edge); }
  .hero-inner { position: absolute; left: 8px; top: 4px; right: 8px; bottom: 0;
    background: radial-gradient(ellipse at 70% 40%, #3c414a 0%, var(--banner) 55%, #262930 100%); }
  .hero-title { position: absolute; left: 85px; top: 67px; font-family: "Orbitron", sans-serif; font-weight: 700;
    font-size: 26px; line-height: 33px; color: var(--white); letter-spacing: 1px; text-transform: uppercase; }
  .hero-copy { position: absolute; left: 85px; top: 133px; width: 405px; font-size: 13.5px; font-weight: 300;
    line-height: 22.3px; color: #f0f0f0; }
  .hero-actions { position: absolute; left: 85px; top: 259px; display: flex; gap: 12px; }
  .btn { display: inline-block; height: 32px; padding: 0 17px; line-height: 30px; font-size: 14px; color: #222;
    background: linear-gradient(#f4f4f4, #dedede); border: 1px solid #bbb; border-radius: 2px; text-decoration: none; }
  .hero-visual { position: absolute; left: 533px; top: 44px; width: 560px; height: 312px;
    background: linear-gradient(180deg, #d8dde3 0%, #b9c2cc 70%, #9aa0a8 100%); border-radius: 10px; }
  .slider-tab { position: absolute; left: 528px; top: 382px; }
  .slider-dots { position: absolute; left: 566px; top: 396px; display: flex; gap: 5px; }
  .slider-dots span { width: 10px; height: 10px; border-radius: 50%; background: #6a6d73; }
  .slider-dots span.is-active { background: var(--white); }

  .feature-row { position: absolute; left: 74px; top: 562px; display: flex; gap: 16px; }
  .feature-card { position: relative; width: 337px; height: 321px; border: 1px solid var(--card-border);
    background: var(--white); box-shadow: 0 6px 6px -4px rgba(0,0,0,0.12); }
  .feature-card:nth-child(3) { margin-left: 3px; }
  .feature-title { position: absolute; left: 19px; top: 21px; font-family: "Orbitron", sans-serif; font-weight: 500;
    font-size: 17px; letter-spacing: 1px; color: #222; text-transform: uppercase; }
  .feature-image { position: absolute; left: 19px; top: 54px; width: 296px; height: 131px; }
  .feature-image.spotlight { background: linear-gradient(90deg, #c9d3dd 0%, #8aa6c4 45%, #163050 75%, #05101e 100%); }
  .feature-image.partners { background: radial-gradient(circle at 50% 50%, #ffffff 0%, #e8b79a 40%, #c47a52 100%); }
  .feature-image.support { background: linear-gradient(90deg, #9fb7d0 0%, #dce6ef 45%, #e8c9ae 75%, #c8d8ea 100%); }
  .feature-text { position: absolute; left: 20px; top: 195px; width: 290px; font-size: 13px; line-height: 19.5px; color: var(--text); }
  .learn-more { position: absolute; left: 18px; top: 265px; font-size: 13.5px; color: var(--accent); text-decoration: none;
    text-transform: uppercase; display: flex; align-items: center; gap: 6px; }

  .site-footer { position: absolute; left: 0; top: 921px; width: 1200px; height: 118px; background: var(--footer-bg); }
  .footer-brand { position: absolute; left: 75px; top: 30px; display: flex; align-items: center; gap: 10px; }
  .footer-brand .brand-mark { width: 30px; height: 30px; }
  .footer-brand .brand-name { font-size: 28px; letter-spacing: 4px; }
  .footer-nav { position: absolute; left: 279px; top: 38px; display: flex; font-size: 13px; color: #111; }
  .footer-nav a { color: #111; text-decoration: none; }
  .footer-nav .slash { margin: 0 12px; }
  .copyright { position: absolute; left: 280px; top: 65px; font-size: 12px; color: #555; }
  .contact-lines { position: absolute; left: 848px; top: 39px; font-size: 13px; line-height: 22px; color: #111; }
  .contact-lines b { font-weight: 400; margin-right: 6px; }
  .social { position: absolute; left: 1021px; top: 36px; display: flex; gap: 3px; }
  .social span { width: 22px; height: 22px; border-radius: 50%; background: #111; }
</style>
</head>
<body>
  <div class="top-rule"></div>

  <header class="site-header">
    <div class="brand">
      <span class="brand-mark"></span>
      <span class="brand-name">TAVELON</span>
    </div>
    <nav class="main-nav">
      <a class="is-current" href="#">Home</a><span class="sep"></span>
      <a href="#">About Us</a><span class="sep"></span>
      <a href="#">Solutions</a><span class="sep"></span>
      <a href="#">Services</a><span class="sep"></span>
      <a href="#">Contact</a>
    </nav>
  </header>

  <section class="hero">
    <div class="hero-inner">
      <h1 class="hero-title">Managed IT Service<br>Professionals</h1>
      <p class="hero-copy">Tavelon Systems employs an innovative managed service solution to provide our clients with technical expertise and superb customer service. Our goal is to ensure that our clients business requirements align with their technical needs in order to maximize their benefits.</p>
      <div class="hero-actions">
        <a class="btn" href="#">Learn More</a>
        <a class="btn" href="#">View Project</a>
      </div>
      <div class="hero-visual" role="img" aria-label="Laptop showing a support agent with a headset working in a bright office"></div>
      <svg class="slider-tab" width="112" height="34" viewBox="0 0 112 34" aria-hidden="true">
        <path d="M0 34 C18 34 18 0 40 0 L72 0 C94 0 94 34 112 34 Z" fill="#1d1f24"/>
      </svg>
      <div class="slider-dots"><span class="is-active"></span><span></span><span></span><span></span></div>
    </div>
  </section>

  <main class="feature-row">
    <article class="feature-card">
      <h2 class="feature-title">Spotlight</h2>
      <div class="feature-image spotlight" role="img" aria-label="Engineer at a desk working with technical drawings on two monitors"></div>
      <p class="feature-text">Lorem ipsum dolor sit amet, consectetuer adipiscing elit. Nam cursus. Morbi ut mi. Nullam enim leo, egestas id, condimentum at.</p>
      <a class="learn-more" href="#">Learn More <svg width="6" height="9" viewBox="0 0 6 9"><path d="M0 0 L6 4.5 L0 9 Z" fill="currentColor"/></svg></a>
    </article>
    <article class="feature-card">
      <h2 class="feature-title">Partners</h2>
      <div class="feature-image partners" role="img" aria-label="Open hands joined together in a circle"></div>
      <p class="feature-text">Lorem ipsum dolor sit amet, consectetuer adipiscing elit. Nam cursus. Morbi ut mi. Nullam enim leo, egestas id, condimentum at.</p>
      <a class="learn-more" href="#">Learn More <svg width="6" height="9" viewBox="0 0 6 9"><path d="M0 0 L6 4.5 L0 9 Z" fill="currentColor"/></svg></a>
    </article>
    <article class="feature-card">
      <h2 class="feature-title">Live Support</h2>
      <div class="feature-image support" role="img" aria-label="Support staff wearing headsets in a call centre"></div>
      <p class="feature-text">Lorem ipsum dolor sit amet, consectetuer adipiscing elit. Nam cursus. Morbi ut mi. Nullam enim leo, egestas id, condimentum at.</p>
      <a class="learn-more" href="#">Learn More <svg width="6" height="9" viewBox="0 0 6 9"><path d="M0 0 L6 4.5 L0 9 Z" fill="currentColor"/></svg></a>
    </article>
  </main>

  <footer class="site-footer">
    <div class="footer-brand">
      <span class="brand-mark"></span>
      <span class="brand-name">TAVELON</span>
    </div>
    <nav class="footer-nav">
      <a href="#">Home</a><span class="slash">/</span>
      <a href="#">About Us</a><span class="slash">/</span>
      <a href="#">Solutions</a><span class="slash">/</span>
      <a href="#">Services</a><span class="slash">/</span>
      <a href="#">Contact Us</a>
    </nav>
    <p class="copyright">© 2012 Company Name. All rights reserved. Term of Use</p>
    <div class="contact-lines">
      <div><b>CALL:</b> 403.555.0182</div>
      <div><b>Email:</b> info@tavelon.com</div>
    </div>
    <div class="social" aria-label="Social links"><span></span><span></span><span></span><span></span></div>
  </footer>
</body>
</html>
```